New (old) Business Card Design Project

I would like to purchase a customized version of a design you have previously submitted - https://www.artsubmitly.example/design/7395021

I like the card above, and would like to use the same design, jus with my business name, BRADLEY ASSET MANAGEMENT. I like the colors in the card above, as well as the font. The other side will have my name, company name, address, phone, email, website, plus disclosure text I will provide.

Target Market(s)

wealthy families

Industry/Entity Type

Financial Services

Contact Information for Business Card

logo on one side, on other my name, company, address, phone, email, website, disclosure language I will provide.

Colors

Designer to choose colors to be used in the design.

Requirements
Must have
• colors: Deep blue and white
Nice to have
• Please see the items I have uploaded, below.
Should not have
• Cheap, tacky look.

```html
<!DOCTYPE html>
<html lang="en">
<head>
<meta charset="utf-8">
<title>Bradley Asset Management – Business Card</title>
<link rel="stylesheet" href="https://fonts.googleapis.com/css2?family=Libre+Baskerville:wght@400;700&family=Roboto:wght@400;500&display=swap">
<style>
  :root {
    --navy: #1f2359;
    --white: #ffffff;
    --ink: #222222;
    --rule: #555555;
    --backdrop: #d9d9dc;
  }
  * { margin: 0; padding: 0; box-sizing: border-box; }
  html, body { width: 1200px; height: 901px; overflow: hidden; }
  body {
    background: var(--backdrop);
    position: relative;
    font-family: "Roboto", Arial, sans-serif;
  }
  .card {
    position: absolute;
    left: 320px;
    width: 560px;
    height: 320px;
    box-shadow: 0 6px 18px rgba(0,0,0,0.25);
  }
  .card--front { top: 95px; background: var(--navy); }
  .card--back  { top: 485px; background: var(--white); }

  .brand-name {
    position: absolute;
    left: 0; right: 0; top: 0; bottom: 0;
    display: flex;
    align-items: center;
    justify-content: center;
    font-family: "Libre Baskerville", Georgia, serif;
    font-weight: 700;
    font-size: 23px;
    letter-spacing: 3px;
    color: var(--white);
  }

  .person {
    position: absolute;
    left: 150px;
    top: 138px;
    text-align: right;
    width: 160px;
  }
  .person__name {
    font-weight: 500;
    font-size: 19px;
    color: var(--navy);
    letter-spacing: 0.3px;
  }
  .person__title {
    font-size: 11px;
    color: var(--ink);
    margin-top: 1px;
  }
  .divider {
    position: absolute;
    left: 330px;
    top: 110px;
    width: 1px;
    height: 100px;
    background: var(--rule);
  }
  .contact {
    position: absolute;
    left: 350px;
    top: 116px;
    font-size: 11px;
    line-height: 17px;
    color: var(--ink);
    list-style: none;
  }
  .contact__web { color: var(--navy); }
</style>
</head>
<body>
  <section class="card card--front" aria-label="Card front">
    <p class="brand-name">BRADLEY ASSET MANAGEMENT</p>
  </section>

  <section class="card card--back" aria-label="Card back">
    <div class="person">
      <p class="person__name">DANIEL WHITFORD</p>
      <p class="person__title">Managing Director</p>
    </div>
    <span class="divider"></span>
    <ul class="contact">
      <li>1480 W Harbor Lane</li>
      <li>Marlow County name 4172</li>
      <li>TEL: 555 014 2286</li>
      <li>EMAIL: info@bradleyasset.example</li>
      <li class="contact__web">www.bradleyasset.example</li>
    </ul>
  </section>
</body>
</html>
```